Double sided business Card voor Luchtkoel Brederwijk

Card design must be in line with our logo. Clean and professional look. Colors can be used, but not too wild.
Logo in frontside. Details on the backside. We want a qr in the design.

Details: (person)
name: Maarten Bosveld
tel: 06-48271935
maarten@luchtkoelbrederwijk.nl

tel: 088-5063918 (business general)
info@luchtkoelbrederwijk.nl

.

```html
<!DOCTYPE html>
<html lang="nl">
<head>
<meta charset="utf-8">
<title>Luchtkoel Brederwijk – visitekaartje</title>
<link rel="stylesheet" href="https://fonts.googleapis.com/css2?family=Arimo:wght@400;700&display=swap">
<style>
  :root {
    --page-bg: #eef0f3;
    --card-white: #ffffff;
    --brand-blue: #1769b3;
    --brand-red: #e5232e;
    --ink-grey: #4d4d4f;
    --on-blue: #ffffff;
    --divider: rgba(255,255,255,0.35);
    --qr-fill: #e4e7ec;
    --qr-edge: #c3c8d0;
  }
  * { box-sizing: border-box; margin: 0; padding: 0; }
  html, body { width: 1200px; height: 1000px; overflow: hidden; }
  body {
    background: var(--page-bg);
    font-family: "Arimo", Arial, sans-serif;
    position: relative;
  }
  .card {
    position: absolute;
    left: 320px;
    width: 560px;
    height: 320px;
    background: var(--card-white);
    box-shadow: 0 6px 14px rgba(0,0,0,0.18);
    overflow: hidden;
  }
  .card--front { top: 144px; }
  .card--back { top: 536px; }

  .brand-dot {
    position: absolute;
    border-radius: 50%;
    background: var(--brand-blue);
  }
  .card--front .brand-dot { width: 96px; height: 96px; left: 232px; top: 66px; }
  .card--back .brand-dot { width: 46px; height: 46px; left: 444px; top: 20px; }

  .wordmark {
    position: absolute;
    color: var(--ink-grey);
    font-weight: 400;
    text-transform: uppercase;
    text-align: center;
    line-height: 1.15;
  }
  .wordmark span { display: block; }
  .card--front .wordmark { left: 0; right: 0; top: 200px; }
  .card--front .wordmark__line1 { font-size: 23px; letter-spacing: 0.14em; }
  .card--front .wordmark__line2 { font-size: 30px; letter-spacing: 0.12em; }
  .card--back .wordmark { left: 362px; width: 210px; top: 88px; }
  .card--back .wordmark__line1 { font-size: 12.5px; letter-spacing: 0.14em; }
  .card--back .wordmark__line2 { font-size: 16px; letter-spacing: 0.12em; }

  .qr-area {
    position: absolute;
    left: 20px;
    top: 20px;
    width: 76px;
    height: 76px;
    background: var(--qr-fill);
    border: 1px solid var(--qr-edge);
  }

  .back-wave { position: absolute; inset: 0; }

  .holder {
    position: absolute;
    left: 22px;
    top: 186px;
    color: var(--on-blue);
  }
  .holder__name { font-size: 27px; font-weight: 700; }
  .holder__role { font-size: 15px; letter-spacing: 0.04em; margin-top: 4px; }

  .contact {
    position: absolute;
    top: 270px;
    color: var(--on-blue);
    font-size: 12.5px;
    line-height: 16px;
  }
  .contact--personal { left: 22px; }
  .contact--office { left: 336px; }
  .contact__row { display: flex; align-items: center; gap: 5px; }
  .contact__row .phone-number { letter-spacing: 0.12em; }
  .contact__row svg { flex: none; }
  .contact__spacer { width: 20px; flex: none; }
  .contact-divider {
    position: absolute;
    left: 280px;
    top: 272px;
    width: 1px;
    height: 28px;
    background: var(--divider);
  }
</style>
</head>
<body>

  <section class="card card--front" aria-label="Voorzijde">
    <div class="brand-dot"></div>
    <div class="wordmark">
      <span class="wordmark__line1">Luchtkoel</span>
      <span class="wordmark__line2">Brederwijk</span>
    </div>
  </section>

  <section class="card card--back" aria-label="Achterzijde">
    <div class="qr-area" role="img" aria-label="QR-code met contactgegevens"></div>

    <svg class="back-wave" viewBox="0 0 560 320" width="560" height="320" aria-hidden="true">
      <path fill="var(--brand-red)" d="M0 156 C 90 118, 200 124, 300 160 S 470 196, 560 172 L560 178 C 470 202, 390 192, 300 166 S 90 128, 0 162 Z"/>
      <path fill="var(--brand-blue)" d="M0 162 C 90 124, 200 130, 300 166 S 470 202, 560 178 L560 320 L0 320 Z"/>
      <path fill="var(--brand-red)" d="M140 140 C 200 138, 255 152, 300 168 S 470 210, 560 184 L560 189 C 470 214, 390 204, 300 174 S 200 142, 140 140 Z"/>
    </svg>

    <div class="brand-dot"></div>
    <div class="wordmark">
      <span class="wordmark__line1">Luchtkoel</span>
      <span class="wordmark__line2">Brederwijk</span>
    </div>

    <div class="holder">
      <div class="holder__name">Maarten Bosveld</div>
      <div class="holder__role">POSITION DETAILS</div>
    </div>

    <div class="contact contact--personal">
      <div class="contact__row">
        <svg width="12" height="12" viewBox="0 0 12 12" aria-hidden="true"><rect x="3" y="0.5" width="6" height="11" rx="1.2" fill="var(--brand-red)"/></svg>
        <span class="phone-number">06-48271935</span>
      </div>
      <div class="contact__row">
        <svg width="12" height="9" viewBox="0 0 12 9" aria-hidden="true"><rect x="0" y="0" width="12" height="9" rx="1" fill="var(--brand-red)"/><path d="M0.5 1 L6 5 L11.5 1" fill="none" stroke="#fff" stroke-width="1"/></svg>
        <span>maarten@luchtkoelbrederwijk.nl</span>
      </div>
    </div>

    <div class="contact-divider"></div>

    <div class="contact contact--office">
      <div class="contact__row">
        <svg width="20" height="16" viewBox="0 0 20 16" aria-hidden="true"><path d="M2 5 Q10 -1 18 5 L16 7 L13 6 L13 5 Q10 3.5 7 5 L7 6 L4 7 Z" fill="var(--brand-red)"/><rect x="3" y="8" width="14" height="8" rx="1.5" fill="var(--brand-red)"/><circle cx="10" cy="12" r="2" fill="#fff"/></svg>
        <span class="phone-number">088-5063918</span>
      </div>
      <div class="contact__row">
        <span class="contact__spacer"></span>
        <span>info@luchtkoelbrederwijk.nl</span>
      </div>
    </div>
  </section>

</body>
</html>
```